we need a business card. We are an online company that provides work life balance services to our members. our website can be viewed at www.quillmoorhub.com.au
Our company logo is attached as well as a business card look that i like.

```html
<!DOCTYPE html>
<html lang="en">
<head>
<meta charset="utf-8">
<title>quillmoorhub business card</title>
<link href="https://fonts.googleapis.com/css2?family=Open+Sans:wght@400;600;800&family=Varela+Round&display=swap" rel="stylesheet">
<style>
  :root {
    --leaf-dark: #2f7a1c;
    --leaf-mid: #4f9a2a;
    --leaf-light: #8cc63f;
    --paper: #ffffff;
    --paper-shade: #eeeeee;
    --ink: #4a4a4a;
    --ink-soft: #777777;
    --backdrop: #e9e6df;
  }
  * { box-sizing: border-box; margin: 0; padding: 0; }
  html, body { width: 1200px; height: 1000px; overflow: hidden; }
  body {
    background: var(--backdrop);
    font-family: "Open Sans", Arial, sans-serif;
    display: flex;
    align-items: center;
    justify-content: center;
    gap: 60px;
  }
  .card {
    position: relative;
    width: 525px;
    height: 300px;
    border-radius: 22px;
    overflow: hidden;
    box-shadow: 0 10px 30px rgba(0,0,0,0.18);
  }

  /* front */
  .card-front {
    background: linear-gradient(125deg, var(--leaf-dark) 0%, var(--leaf-mid) 40%, var(--leaf-light) 62%, var(--leaf-mid) 80%, var(--leaf-dark) 100%);
  }
  .card-front .waves { position: absolute; inset: 0; }
  .brand {
    position: absolute;
    left: 50%; top: 50%;
    transform: translate(-50%, -50%);
    display: flex;
    align-items: center;
    gap: 16px;
    color: var(--paper);
  }
  .brand-dot {
    width: 54px; height: 54px;
    border-radius: 50%;
    background: var(--paper);
  }
  .brand-name {
    font-family: "Varela Round", "Open Sans", sans-serif;
    font-size: 46px;
    letter-spacing: 0.5px;
  }

  /* back */
  .card-back { background: linear-gradient(180deg, var(--paper) 0%, var(--paper-shade) 100%); }
  .card-back .band {
    position: absolute;
    left: 0; right: 0; bottom: 0;
    height: 56px;
  }
  .back-brand {
    position: absolute;
    left: 28px; top: 66px;
    width: 180px;
    display: flex;
    flex-direction: column;
    align-items: center;
    gap: 12px;
  }
  .back-brand .brand-dot { width: 84px; height: 84px; background: var(--leaf-light); }
  .back-brand .brand-name { font-size: 24px; color: var(--leaf-mid); }
  .divider {
    position: absolute;
    left: 222px; top: 30px;
    width: 1px; height: 190px;
    background: #9a9a9a;
  }
  .contact {
    position: absolute;
    left: 244px; top: 30px;
    right: 20px;
  }
  .person-first {
    font-size: 30px; font-weight: 800;
    color: var(--leaf-mid);
    line-height: 1;
    letter-spacing: 0.5px;
  }
  .person-last {
    font-size: 22px; font-weight: 800;
    color: var(--ink);
    line-height: 1.1;
  }
  .person-role {
    font-size: 10px; color: var(--ink-soft);
    margin: 2px 0 10px;
  }
  .details { list-style: none; }
  .details li {
    display: flex; align-items: center; gap: 8px;
    font-size: 11px; color: var(--ink);
    line-height: 1.35;
    margin-bottom: 4px;
  }
  .details .pair { gap: 14px; }
  .details .pair span { display: flex; align-items: center; gap: 6px; }
  .details svg { width: 10px; height: 10px; flex: none; fill: var(--leaf-mid); }
</style>
</head>
<body>

  <section class="card card-front" aria-label="Card front">
    <svg class="waves" viewBox="0 0 525 300" preserveAspectRatio="none" aria-hidden="true">
      <path d="M0 90 C150 20 300 200 525 60 L525 0 L0 0Z" fill="#ffffff" opacity="0.07"/>
      <path d="M0 220 C180 120 330 260 525 150 L525 300 L0 300Z" fill="#ffffff" opacity="0.06"/>
      <path d="M0 260 C200 200 350 300 525 230 L525 300 L0 300Z" fill="#000000" opacity="0.08"/>
    </svg>
    <div class="brand">
      <div class="brand-dot"></div>
      <span class="brand-name">quillmoorhub</span>
    </div>
  </section>

  <section class="card card-back" aria-label="Card back">
    <div class="back-brand">
      <div class="brand-dot"></div>
      <span class="brand-name">quillmoorhub</span>
    </div>
    <div class="divider"></div>
    <div class="contact">
      <p class="person-first">MARCEL</p>
      <p class="person-last">DUFRANE</p>
      <p class="person-role">Director</p>
      <ul class="details">
        <li class="pair">
          <span><svg viewBox="0 0 10 10"><path d="M2 0h2l1 3-1.5 1a6 6 0 0 0 2.5 2.5L7 5l3 1v2a2 2 0 0 1-2 2A8 8 0 0 1 0 2a2 2 0 0 1 2-2z"/></svg>02 9555 0142</span>
          <span><svg viewBox="0 0 10 10"><rect x="1" y="3" width="8" height="6" rx="1"/><rect x="2.5" y="0" width="5" height="3"/></svg>02 9555 0187</span>
        </li>
        <li><svg viewBox="0 0 10 10"><rect x="0" y="2" width="10" height="7" rx="1"/></svg>info@quillmoorhub.com.au</li>
        <li><svg viewBox="0 0 10 10"><circle cx="5" cy="5" r="5"/></svg>www.quillmoorhub.com.au</li>
        <li><svg viewBox="0 0 10 10"><path d="M5 0a3.5 3.5 0 0 1 3.5 3.5C8.5 6 5 10 5 10S1.5 6 1.5 3.5A3.5 3.5 0 0 1 5 0z"/></svg>First Floor, 48 Harbour View Road</li>
        <li style="padding-left:18px">Lavender Point, NSW 2061</li>
      </ul>
    </div>
    <svg class="band" viewBox="0 0 525 56" preserveAspectRatio="none" aria-hidden="true">
      <defs>
        <linearGradient id="bandFill" x1="0" y1="0" x2="1" y2="0">
          <stop offset="0" stop-color="#2f7a1c"/>
          <stop offset="0.5" stop-color="#6fb232"/>
          <stop offset="1" stop-color="#3d8a22"/>
        </linearGradient>
      </defs>
      <path d="M0 18 C150 0 330 30 525 8 L525 56 L0 56Z" fill="url(#bandFill)"/>
      <path d="M0 30 C180 14 340 40 525 22 L525 56 L0 56Z" fill="#ffffff" opacity="0.08"/>
    </svg>
  </section>

</body>
</html>
```